Flyer / Small Safety "Poster" (A4 or 8.5x11" paper)

We're looking to create a series of safety signs for woodworkers to print on home printers using standard sized paper (A4 or 8.5x11" depending on where they are), or possibly to have printed on 17x22" paper.
Currently we want only the first one, but keep in mind that all should work together.
They need: Simple graphic. Bold Text. Company logo. Use company colors (orange, black, white.)
To begin, we will start with a single sign for hearing protection. Graphic or clip art to portray either ear plugs or ear-muff design. Text to say, "Hearing Protection is a Sound Investment."

Target Market(s)

USA Woodworkers & CNC Machinists - Male, 20-65 years old

Font styles to use
Sans Serif

Colors
f37122

Requirements
Must have
• Client logo
Nice to have
• Use client colors of black, white, & orange

```html
<!DOCTYPE html>
<html lang="en">
<head>
<meta charset="utf-8">
<title>Hearing Protection Safety Sign</title>
<link rel="stylesheet" href="https://fonts.googleapis.com/css2?family=Montserrat:wght@800;900&display=swap">
<style>
  :root {
    --brand-orange: #f37122;
    --brand-black: #0b0b0b;
    --brand-white: #ffffff;
    --backdrop: #9a9b9d;
    --photo-warm: #b58f6e;
    --photo-deep: #5c4638;
  }
  html, body {
    margin: 0;
    padding: 0;
    width: 1200px;
    height: 1200px;
    overflow: hidden;
    background: var(--backdrop);
  }
  .canvas {
    position: relative;
    width: 1200px;
    height: 1200px;
  }
  .safety-sign {
    position: absolute;
    left: 213px;
    top: 91px;
    width: 789px;
    height: 1016px;
  }
  .safety-sign svg {
    display: block;
    width: 100%;
    height: 100%;
  }
  .sign-type {
    font-family: "Montserrat", Arial, sans-serif;
    font-weight: 900;
  }
  .brand-name {
    font-family: "Montserrat", Arial, sans-serif;
    font-weight: 800;
    fill: var(--brand-black);
  }
</style>
</head>
<body>
<main class="canvas">
  <section class="safety-sign" aria-label="Hearing protection is a sound investment">
    <svg viewBox="0 0 789 1016" xmlns="http://www.w3.org/2000/svg">
      <defs>
        <linearGradient id="photoTone" x1="0" y1="0" x2="1" y2="1">
          <stop offset="0" stop-color="var(--photo-warm)"/>
          <stop offset="0.55" stop-color="#8a6a52"/>
          <stop offset="1" stop-color="var(--photo-deep)"/>
        </linearGradient>
      </defs>

      <!-- photo area -->
      <polygon class="photo-area" role="img"
        aria-label="Photo of a worker in a hi-vis vest and safety glasses wearing yellow ear muffs"
        points="0,340 789,140 789,620 0,790" fill="url(#photoTone)"/>

      <!-- top orange band -->
      <polygon class="band-top" points="0,0 789,0 789,156 0,356" fill="var(--brand-orange)"/>

      <!-- bottom black band with orange edge -->
      <polygon class="band-edge" points="0,764 789,591 789,606 0,779" fill="var(--brand-orange)"/>
      <polygon class="band-bottom" points="0,776 789,603 789,1016 0,1016" fill="var(--brand-black)"/>

      <!-- headphone icon -->
      <g class="icon-headphones" fill="none" stroke="var(--brand-white)" stroke-width="7" stroke-linejoin="round" stroke-linecap="round">
        <path d="M44,92 V74 a44,44 0 0 1 88,0 V92"/>
        <rect x="34" y="86" width="22" height="38" rx="6"/>
        <rect x="120" y="86" width="22" height="38" rx="6"/>
        <rect x="46" y="80" width="10" height="50" rx="4"/>
        <rect x="120" y="80" width="10" height="50" rx="4"/>
      </g>

      <!-- headline -->
      <g class="headline" transform="translate(42,212) rotate(-12)">
        <text class="sign-type" x="0" y="0" font-size="82" fill="var(--brand-white)"
          textLength="430" lengthAdjust="spacingAndGlyphs">HEARING</text>
        <rect x="-80" y="8" width="180" height="9" fill="var(--brand-white)"/>
        <text class="sign-type" x="90" y="95" font-size="92" fill="var(--brand-black)"
          textLength="630" lengthAdjust="spacingAndGlyphs">PROTECTION</text>
        <rect x="90" y="103" width="720" height="9" fill="var(--brand-black)"/>
      </g>

      <!-- brand seal -->
      <g class="brand-seal">
        <circle cx="602" cy="662" r="126" fill="var(--brand-white)" stroke="var(--brand-orange)" stroke-width="9"/>
        <text class="brand-name" x="602" y="656" font-size="32" text-anchor="middle">TARNVALE</text>
        <text class="brand-name" x="602" y="694" font-size="32" text-anchor="middle">TOOLS</text>
      </g>

      <!-- tick badge -->
      <g class="tick-badge">
        <circle cx="97" cy="889" r="60" fill="var(--brand-white)"/>
        <circle cx="97" cy="889" r="50" fill="var(--brand-orange)"/>
        <path d="M72,890 L91,909 L124,872" fill="none" stroke="var(--brand-white)" stroke-width="11" stroke-linecap="round" stroke-linejoin="round"/>
      </g>

      <!-- tagline -->
      <text class="sign-type" x="187" y="896" font-size="90" textLength="560" lengthAdjust="spacingAndGlyphs">
        <tspan fill="var(--brand-white)">IS </tspan><tspan fill="var(--brand-orange)">A SOUND</tspan>
      </text>
      <text class="sign-type" x="187" y="964" font-size="90" fill="var(--brand-white)"
        textLength="560" lengthAdjust="spacingAndGlyphs">INVESTMENT</text>
      <rect class="tagline-rule" x="187" y="970" width="602" height="8" fill="var(--brand-white)"/>
    </svg>
  </section>
</main>
</body>
</html>
```